Honey Bottle Labels for Honey Business

The honey is a niche product and the logo should exude a strong impression of wild and raw honey and natural – as in natural beekeeping. We try to keep things as simple as possible; this includes the processes the honey goes through.
We are looking for something with a gourmet / classy upmarket look and feel design. For example: Ideas with bees, honeycomb, modern or hexagonal feature; something eye catching, but not too busy.
Our honey is all natural and organic. We are a clean, simple yet sophisticated business, so would like our logo to reflect these principles.

Feel free to expand your creativity to anything you may think would look awesome and original!

The label needs to contain:
1. Our company logo. (Please see attached)
2. 100% Pure Raw Honey / Local
3. Net Wt: 16 oz (454 g) (this is the weight of the honey and will need to be modified based on bottle size.)
4. Address, Maple Ridge, MN 55999 (not larger than 1/16th inch)

Needs to be versatile to include possibility of clear label, I have included some example pictures as ideas (oval, round, square tags)

Sizes needed:
Large oval 2 5/8" x 4 1/2"
Small oval: 1 3/4" wide x 3" tall
Rectangle 1 3/4" tall x 5" wide
Round diameter 2.5"

Target Market(s)

Gourmet stores, market stall, local tourist market, potential store door sales

Requirements
Must have
• - A design that can be used on various packaging, jars and containers. We are hoping to scale up the production and want something to suit.
• - has to have a wow to stand out on the supermarket shelves
Nice to have
• Things we like:
• Minimalist designs
• Clever designs
• We don't like hand drawn font types
• We are open to the use of a hexagon in the logo, but not must have
Should not have
• Things we do not like:
• Too many colors

```html
<!DOCTYPE html>
<html lang="en">
<head>
<meta charset="utf-8">
<title>Golden Meadow Honey – Round Jar Label</title>
<link rel="stylesheet" href="https://fonts.googleapis.com/css2?family=Ubuntu:wght@400;500;700&display=swap">
<style>
  :root {
    --page-bg: #f3f3f2;
    --label-white: #ffffff;
    --honey-light: #fcbc2f;
    --honey-deep: #f39c12;
    --honey-ring: #f7a81b;
    --brown-ink: #3a2413;
    --bee-tone: #f6ead6;
  }
  html, body {
    margin: 0;
    padding: 0;
    width: 1200px;
    height: 1200px;
    overflow: hidden;
    background: var(--page-bg);
  }
  .canvas {
    width: 1200px;
    height: 1200px;
    display: block;
  }
  .arc-text {
    font-family: "Ubuntu", sans-serif;
    font-weight: 700;
    fill: var(--brown-ink);
    letter-spacing: 3px;
  }
  .arc-text--claim { font-size: 50px; }
  .arc-text--address { font-size: 34px; letter-spacing: 4px; }
  .brand-name {
    font-family: "Ubuntu", sans-serif;
    font-weight: 400;
    font-size: 66px;
    fill: var(--honey-ring);
  }
</style>
</head>
<body>
<svg class="canvas" viewBox="0 0 1200 1200" xmlns="http://www.w3.org/2000/svg">
  <defs>
    <radialGradient id="honeyFill" cx="50%" cy="45%" r="55%">
      <stop offset="0%" stop-color="var(--honey-light)"/>
      <stop offset="100%" stop-color="var(--honey-deep)"/>
    </radialGradient>
    <path id="topArc" d="M205,600 A395,395 0 0 1 995,600"/>
    <path id="bottomArc" d="M180,600 A420,420 0 0 0 1020,600"/>
  </defs>

  <g class="label">
    <circle class="label__edge" cx="600" cy="600" r="505" fill="var(--label-white)"/>
    <circle class="label__field" cx="600" cy="600" r="470" fill="url(#honeyFill)"
            role="img" aria-label="Honeycomb hexagon pattern in honey tones"/>

    <path class="label__dash" d="M228.8,464.9 A395,395 0 0 0 402.5,942.1"
          fill="none" stroke="var(--brown-ink)" stroke-width="2.5" stroke-dasharray="9 7"/>
    <path class="label__dash" d="M971.2,464.9 A395,395 0 0 1 797.5,942.1"
          fill="none" stroke="var(--brown-ink)" stroke-width="2.5" stroke-dasharray="9 7"/>

    <polygon class="label__hex" fill="var(--brown-ink)"
             points="183,600 194,581 216,581 227,600 216,619 194,619"/>
    <polygon class="label__hex" fill="var(--brown-ink)"
             points="973,600 984,581 1006,581 1017,600 1006,619 984,619"/>

    <text class="arc-text arc-text--claim">
      <textPath href="#topArc" startOffset="29%" text-anchor="middle">100% PURE</textPath>
    </text>
    <text class="arc-text arc-text--claim">
      <textPath href="#topArc" startOffset="71%" text-anchor="middle">RAW HONEY</textPath>
    </text>
    <text class="arc-text arc-text--address">
      <textPath href="#bottomArc" startOffset="50%" text-anchor="middle">MAPLE RIDGE, MN 55999</textPath>
    </text>

    <circle class="label__center" cx="600" cy="640" r="258"
            fill="var(--label-white)" stroke="var(--honey-ring)" stroke-width="9"/>

    <ellipse class="label__bee" cx="600" cy="255" rx="105" ry="100"
             fill="var(--bee-tone)" role="img"
             aria-label="Illustration of a honeybee with spread wings, seen from above"/>

    <text class="brand-name" x="600" y="650" text-anchor="middle">golden meadow</text>
    <text class="brand-name" x="600" y="730" text-anchor="middle">honey</text>
  </g>
</svg>
</body>
</html>
```